Unternehmensberatung sucht Kartendesign für Seminarspiel
Zielgruppe
Projekt: Kartenspiel Seminarspiel für Führungskräfte / Trainerbedarf
Wir sind eine Unternehmensberatung, die Führungskräfte und Unternehmen in Veränderungsprozessen begleitet.
Aufgabenstellung
Desgin: in DIN A6 als Druckvorlage bzw. zur Verwendung der Bilddateien.
ZU designen: 1 Rückseite:
ca. 9 Vorderseiten-Designs, div. Texte -> 60 Seiten
1 Verpackung

```html
<!DOCTYPE html>
<html lang="de">
<head>
<meta charset="utf-8">
<title>Seminarspiel – Kartenübersicht</title>
<link rel="stylesheet" href="https://fonts.googleapis.com/css2?family=Arimo:wght@400&family=Noto+Sans:wght@700&display=swap">
<style>
:root{
  --bg:#737373;
  --white:#ffffff;
  --ink:#1a1a1a;
  --staerken:#1d71b8;
  --sicherheit:#fdcd20;
  --kommunikation:#e31e24;
  --kultur:#0e8c55;
  --mindset:#5a2d62;
  --resilienz:#ee7837;
  --sinn:#009fe3;
  --lead:#9189b3;
}
*{margin:0;padding:0;box-sizing:border-box}
html,body{width:1200px;height:912px;overflow:hidden;background:var(--bg)}
.sheet{position:relative;width:1200px;height:912px}
.card{position:absolute;width:246px;height:174px;overflow:hidden}
.col-1{left:42px}.col-2{left:339px}.col-3{left:628px}.col-4{left:911px}
.row-front-1{top:65px}.row-back-1{top:256px}.row-front-2{top:477px}.row-back-2{top:668px}

.front{background:var(--white)}
.front .wave{position:absolute;left:0;top:0;width:246px;height:174px}
.front .task{position:absolute;left:20px;right:20px;top:18px;text-align:center;
  font-family:"Arimo",Arial,sans-serif;font-size:10.6px;line-height:11.9px;color:var(--ink)}
.front .task.dense{font-size:8.6px;line-height:9.8px;top:16px;left:14px;right:14px}
.front .note{position:absolute;left:18px;right:18px;top:122px;bottom:6px;display:flex;
  align-items:center;justify-content:center;text-align:center;
  font-family:"Arimo",Arial,sans-serif;font-size:5.4px;line-height:6.5px;color:var(--white)}
.front .note.high{top:116px}

.back{display:flex;align-items:center;justify-content:center;text-align:center}
.back .title{font-family:"Noto Sans",Verdana,sans-serif;font-weight:700;
  font-size:24px;line-height:26px;color:var(--white);white-space:nowrap}

.c-staerken{--accent:var(--staerken)}
.c-sicherheit{--accent:var(--sicherheit)}
.c-kommunikation{--accent:var(--kommunikation)}
.c-kultur{--accent:var(--kultur)}
.c-mindset{--accent:var(--mindset)}
.c-resilienz{--accent:var(--resilienz)}
.c-sinn{--accent:var(--sinn)}
.c-lead{--accent:var(--lead)}
.back{background:var(--accent)}
.wave path{fill:var(--accent)}
</style>
</head>
<body>
<main class="sheet">

  <!-- Reihe 1: Vorderseiten -->
  <article class="card front col-1 row-front-1 c-staerken">
    <svg class="wave" viewBox="0 0 246 174"><path d="M0 112 Q123 140 246 112 L246 174 L0 174Z"/></svg>
    <p class="task">a.<br>Stärkenbrille: Fokussiere Dich in Deinen Gesprächen darauf, Deinem Gesprächspartner am Ende eine wertvolle Stärke zurückzumelden, die Dir an Ihm auffällt.</p>
    <p class="note">Sorge dafür, dass Deine Mitarbeiter bei der Arbeit das tun können, was sie am besten können! Der Stärkenfokus ist zentral im Positive Leadership-Ansatz und hat, wenn konsequent angewandt, verschiedene positive Effekte in Unternehmen wie die Steigerung der Produktivität und des Wohlbefindens des Einzelnen, die Verbesserung der Mitarbeiterbindung und der Senkung des Krankenstandes.</p>
  </article>

  <article class="card front col-2 row-front-1 c-sicherheit">
    <svg class="wave" viewBox="0 0 246 174"><path d="M0 112 Q123 140 246 112 L246 174 L0 174Z"/></svg>
    <p class="task">a.<br>Offenheit: Offenheit schafft Vertrauen. Fokussiere Dich auf etwas, das Dich gerade beschäftigt. Teile Deine Gedanken mit einer Person, die diese Offenheit von Deiner Seite bislang nicht kennt.</p>
    <p class="note">Mit großem Abstand gehören im Lumora Projekt Perikles Psychologische Sicherheit und Vertrauen zu den wichtigste Einflussfaktoren für die Entfaltung der Leistungsfähigkeit in Unternehmen.</p>
  </article>

  <article class="card front col-3 row-front-1 c-kommunikation">
    <svg class="wave" viewBox="0 0 246 174"><path d="M0 112 Q123 140 246 112 L246 174 L0 174Z"/></svg>
    <p class="task">a.<br>Gebe jemandem konstruktives Feedback inkl. einem motivierenden Hinweis zur Verbesserung.</p>
    <p class="note">1. Sorge für eine wertschätzende und auf positive Abweichungen konzentrierte Kommunikation. Die „Positive Kommunikation“ ist eine von vier Säulen innerhalb des Leadership Ansatzes „Positive Organizational Scholarship“ nach Lena Carwell. Die anderen drei Säulen sind übrigens Positive Beziehungen, Positives Klima und Positiver Sinn.</p>
  </article>

  <article class="card front col-4 row-front-1 c-kultur">
    <svg class="wave" viewBox="0 0 246 174"><path d="M0 112 Q123 140 246 112 L246 174 L0 174Z"/></svg>
    <p class="task">a.<br>Gib Deinen Teamkollegen ein wertschätzendes, konkretes Feedback, in dem Du ihren Beitrag zum Gesamtziel des Teams betonst!</p>
    <p class="note">Sorge für eine Kultur in Deinem Umfeld, in der die positiven Emotionen die negativen überwiegen. Die Forschung von Hanna Wellbrook lehrt uns viel über den Wert positiver Emotionen. In einer positiven Kultur sind die Mitarbeiter optimistischer und weniger ängstlich, was u.a. einen positiven Einfluss auf die Produktivität und die Kreativität hat.</p>
  </article>

  <!-- Reihe 1: Rückseiten -->
  <section class="card back col-1 row-back-1 c-staerken"><h2 class="title">Stärken</h2></section>
  <section class="card back col-2 row-back-1 c-sicherheit"><h2 class="title">Sicherheit<br>und Vertrauen</h2></section>
  <section class="card back col-3 row-back-1 c-kommunikation"><h2 class="title">Positive<br>Kommunikation</h2></section>
  <section class="card back col-4 row-back-1 c-kultur"><h2 class="title">Positive Kultur</h2></section>

  <!-- Reihe 2: Vorderseiten -->
  <article class="card front col-1 row-front-2 c-mindset">
    <svg class="wave" viewBox="0 0 246 174"><path d="M0 112 Q123 140 246 112 L246 174 L0 174Z"/></svg>
    <p class="task">a.<br>Achte auf Deine Sprache. Achte auf Deine Worte und Gedanken. Ersetze negative Wörter und Gedanken durch positive und konstruktive Worte.</p>
    <p class="note">Sorge dafür, dass alle Teammitglieder daran glauben, dass sie ihre Fähigkeiten weiterentwickeln dürfen und können und sie auch Schwierigkeiten überwinden können. Die Forschung von Clara Denholm lehrt uns viel über die günstigen Auswirkungen eines Growth Mindset.</p>
  </article>

  <article class="card front col-2 row-front-2 c-resilienz">
    <svg class="wave" viewBox="0 0 246 174"><path d="M0 112 Q123 140 246 112 L246 174 L0 174Z"/></svg>
    <p class="task">a.<br>Verbessere die sozialen Beziehungen in Deinem Team. Was kannst Du dafür tun, um bessere und verbindlichere Beziehungen in Deinem Team zu schaffen?</p>
    <p class="note">Wenn Menschen in belastenden Situationen psychisch stabil bleiben und sich von Rückschlägen zügig erholen, nennen Psychologen diese Fähigkeit "Resilienz". Resiliente Menschen sind beruflich erfolgreicher, emotional stabiler sowie körperlich und psychisch gesünder.</p>
  </article>

  <article class="card front col-3 row-front-2 c-sinn">
    <svg class="wave" viewBox="0 0 246 174"><path d="M0 112 Q123 140 246 112 L246 174 L0 174Z"/></svg>
    <p class="task">a.<br>Klarheit: Wie kannst Du Klarheit über die Unternehmensziele bei den Mitarbeitern erzeugen und steigern?</p>
    <p class="note">1. Gute Führung als Sinnquelle durch KLARMA – ein Ansatz, den Prof. Nils Rosbach gemeinsam mit dem US-Amerikanischen Forscher Martin Stellberg enzwickelt hat. KLARMA steht für Klarheit, Authentizität, Aktualisierung, Respekt, Mehrwert und Autonomie.</p>
  </article>

  <article class="card front col-4 row-front-2 c-lead">
    <svg class="wave" viewBox="0 0 246 174"><path d="M0 112 Q123 140 246 112 L246 174 L0 174Z"/></svg>
    <p class="task dense">a.<br>Positive Emotions: Zufriedene Mitarbeiter sind produktiver (Win-Win Kombination), unzufriedene unproduktiver (Lose-Lose Kombination)? Stimmt grundsätzlich. Es gibt aber auch zufriedene/unproduktive (Komfortzonen-Kombination) und unzufriedene/produktive („Ich bin bald weg“ – Kombination). Betrachte Dein Team und schätze ein, wo Deine Mitarbeiter sich derzeit befinden. Was kannst Du tun, damit möglichst viele in den zufrieden/produktiv Bereich aufsteigen?</p>
    <p class="note high">Das PRISMA-Modell von Professor Selmann wurde in der Forschung von Dr. Mirko Ebbing durch den Faktor „Stärkenorientiertes Führen“ zum PRISMA-LEAD Modell erweitert. Somit können konkrete Verhaltensweisen einer Führungskraft beschrieben werden und das Ausmaß, in dem Führungskräfte ihren MitarbeiterInnen ermöglichen, ihre Potentiale zu entfalten und ihre Stärken im Unternehmen einzubringen.</p>
  </article>

  <!-- Reihe 2: Rückseiten -->
  <section class="card back col-1 row-back-2 c-mindset"><h2 class="title">Growth Mindset</h2></section>
  <section class="card back col-2 row-back-2 c-resilienz"><h2 class="title">Resilienz</h2></section>
  <section class="card back col-3 row-back-2 c-sinn"><h2 class="title">Sinn</h2></section>
  <section class="card back col-4 row-back-2 c-lead"><h2 class="title">PRISMA-Lead</h2></section>

</main>
</body>
</html>
```